SEO Agentur www.findeprofi.de - Webseite soll neu designed werden (Start- und Unterseite)
Zielgruppe
Alle Infos sind auf der Seite www.findeprofi.de enthalten.
Aufgabenstellung
Die Seite soll neu gestalltet werden. Wir möchten gerne ein wenig professioneller werden. Der Name der Seite zwingt uns allerdings ein gewisses Thema auf.
Die Aufgabe:
Ein professionelleres Design der Startseite und einer Unterseite. Die Programmierung machen wir selbst. Thema Suche und Helden muss bleiben aufgrund der URL.
Mit dem Gewinner würden wir dann auch geren jedes Element der Seite durchgehen und neu gestallten (separater Auftrag).
Das Blitzwolf Logo ist aufgrund des neuen Films auch gewaltiger und seriöser geworden. Vielleicht kann man daran anknüpfen. Ist aber keine Bedingung nur eine kleine Idee.
Wir werden alle Vorschläge ca. 50 Leuten vorstellen und dann den Vorschlag mit den meisten Stimmen wählen.

```html
<!DOCTYPE html>
<html lang="de">
<head>
<meta charset="utf-8">
<title>SEO Agentur Findeprofi</title>
<link href="https://fonts.googleapis.com/css2?family=Open+Sans:wght@400;600;700&display=swap" rel="stylesheet">
<style>
:root{
  --ink:#2b2d30;
  --topbar:#34373b;
  --blue:#1aa9ea;
  --blue-dark:#0b84c6;
  --blue-deep:#0a5f9c;
  --red:#d0111b;
  --page:#eef1f6;
  --hero-a:#a9c6de;
  --hero-b:#eef0f4;
  --white:#ffffff;
  --text:#4a4d52;
}
*{box-sizing:border-box;margin:0;padding:0}
html,body{width:1200px;height:895px;overflow:hidden;background:var(--page);font-family:"Open Sans",sans-serif;color:var(--ink)}
.site{position:relative;width:1200px;height:895px;overflow:hidden}

.meta-bar{position:absolute;top:0;left:0;width:100%;height:30px;background:var(--topbar);border-bottom:1px solid #222}
.meta-links{position:absolute;left:225px;top:0;display:flex;height:30px;align-items:center;gap:0}
.meta-links a{color:#e6e8ea;font-size:9px;text-decoration:none;padding:0 12px;border-right:1px solid #55585d;text-transform:uppercase}
.meta-links a:last-child{border:none}
.search{position:absolute;right:220px;top:6px;width:170px;height:18px;border-radius:4px;background:var(--blue);border:1px solid #6dcdf5}
.search svg{position:absolute;right:6px;top:2px}

.nav-band{position:absolute;top:30px;left:0;width:100%;height:52px;background:linear-gradient(#3cc0f5,var(--blue) 50%,var(--blue-dark));box-shadow:0 3px 6px rgba(0,0,0,.25);z-index:3}
.main-nav{position:absolute;left:398px;top:0;height:52px;display:flex;align-items:center}
.main-nav a{color:#12324a;font-size:11.5px;font-weight:600;text-decoration:none;padding:0 10px;border-right:1px solid rgba(10,60,100,.35);text-transform:uppercase}
.main-nav a:last-child{border:none}

.brand{position:absolute;left:226px;top:30px;width:118px;height:90px;background:linear-gradient(#34373b,#1f2124);box-shadow:0 3px 8px rgba(0,0,0,.4);z-index:4;display:flex;flex-direction:column;align-items:center;padding-top:8px;gap:12px}
.brand-name{color:var(--blue);font-weight:700;font-size:15px}
.brand-mark{width:26px;height:26px;border-radius:50%;background:var(--blue)}

.hero{position:absolute;top:82px;left:0;width:100%;height:358px;background:linear-gradient(90deg,var(--hero-a) 0%,var(--hero-b) 40%,#e4e8ee 65%,#b9d1e6 100%)}
.hero-photo{position:absolute;right:140px;top:0;width:340px;height:358px;background:radial-gradient(ellipse at 50% 60%,#6b7a8a 0%,#2e343b 55%,rgba(60,70,80,0) 75%)}
.hero-copy{position:absolute;left:225px;top:48px;width:420px}
.hero-copy h1{font-size:34px;font-weight:400;color:var(--ink);letter-spacing:-.5px}
.hero-copy .claim{color:var(--red);font-size:16.5px;margin-top:12px}
.hero-copy p{font-size:17px;line-height:21px;color:#33363a;margin-top:18px}
.hero-copy p strong{font-weight:600}
.btn{display:inline-block;margin-top:16px;background:linear-gradient(#2cb6f1,var(--blue-dark));color:#0c2d46;font-size:13px;padding:10px 18px;border:1px solid var(--blue-deep);text-transform:uppercase}
.arrow{position:absolute;top:212px;width:34px;height:34px;border-radius:50%;background:var(--white);box-shadow:0 1px 4px rgba(0,0,0,.3)}
.arrow.prev{left:98px}.arrow.next{right:108px}
.arrow svg{position:absolute;left:9px;top:8px}
.dots{position:absolute;left:782px;top:353px;display:flex;gap:8px}
.dots i{width:9px;height:9px;border-radius:50%;background:#2a2d31}
.dots i:first-child{background:var(--blue)}

.section-tab{position:absolute;left:628px;top:436px;width:318px;height:60px;background:linear-gradient(#29b5f1,var(--blue-dark));box-shadow:0 3px 6px rgba(0,0,0,.3);display:flex;align-items:center;justify-content:center;color:#0b2a42;font-size:17px;text-transform:uppercase;z-index:2}

.services{position:absolute;top:540px;left:0;width:100%;display:flex;justify-content:center;gap:70px}
.service{width:230px;text-align:center}
.service h2{font-size:21px;font-weight:400;color:var(--blue-dark);margin-top:12px;text-transform:uppercase}
.service p{font-size:13.5px;line-height:21px;color:var(--text);margin-top:10px}
.service p em{font-style:normal;color:var(--red);font-weight:600}
</style>
</head>
<body>
<div class="site">
  <header>
    <div class="meta-bar">
      <nav class="meta-links"><a href="#">Impressum</a><a href="#">Über uns</a><a href="#">Kontakt</a></nav>
      <div class="search"><svg width="12" height="12" viewBox="0 0 12 12"><circle cx="5" cy="5" r="3.6" fill="none" stroke="#0c3552" stroke-width="1.4"/><line x1="7.6" y1="7.6" x2="11" y2="11" stroke="#0c3552" stroke-width="1.6"/></svg></div>
    </div>
    <div class="nav-band">
      <nav class="main-nav">
        <a href="#">Ablauf</a><a href="#">Ihre Vorteile</a><a href="#">Unsere Leistungen</a><a href="#">100 % Geld-Zurück-Garantie</a><a href="#">Infos</a><a href="#">Blog</a><a href="#">Kontakt</a>
      </nav>
    </div>
    <a class="brand" href="#"><span class="brand-name">findeprofi.de</span><span class="brand-mark"></span></a>
  </header>

  <section class="hero">
    <div class="hero-photo" role="img" aria-label="Foto: junger Mann im Anzug öffnet sein Hemd, darunter ein Heldenkostüm"></div>
    <div class="hero-copy">
      <h1>SEO Agentur Findeprofi</h1>
      <div class="claim">Erfolgsbasiert und mit 100% Geld-Zurück-Garantie</div>
      <p>Wir halten was wir versprechen – <strong>GARANTIERT!</strong><br>Als einer der wenigen Anbieter geben wir Ihnen eine 100% Geld-Zurück-Garantie!</p>
      <a class="btn" href="#">Weiter lesen</a>
    </div>
    <span class="arrow prev"><svg width="16" height="18" viewBox="0 0 16 18"><path d="M11 2 4 9l7 7" fill="none" stroke="var(--blue-dark)" stroke-width="3"/></svg></span>
    <span class="arrow next"><svg width="16" height="18" viewBox="0 0 16 18"><path d="M5 2l7 7-7 7" fill="none" stroke="var(--blue-dark)" stroke-width="3"/></svg></span>
    <div class="dots"><i></i><i></i><i></i><i></i></div>
  </section>

  <div class="section-tab">Unsere Leistungen im Überblick</div>

  <section class="services">
    <article class="service">
      <svg width="70" height="70" viewBox="0 0 70 70"><circle cx="35" cy="35" r="28" fill="none" stroke="var(--blue-dark)" stroke-width="6"/><path d="M35 35V15a20 20 0 1 0 18 12z" fill="var(--blue-dark)"/></svg>
      <h2>Keyword-Analyse</h2>
      <p>Im Rahmen einer <em>detaillierten Analyse</em> Ihrer Webseite identifizieren wir mit Hilfe unserer Tools die für Sie relevanten Keywords. Sie erhalten von uns eine Übersicht mit den wichtigsten Begriffen.</p>
    </article>
    <article class="service">
      <svg width="70" height="70" viewBox="0 0 70 70"><circle cx="29" cy="29" r="19" fill="none" stroke="var(--blue-dark)" stroke-width="6"/><line x1="43" y1="43" x2="62" y2="62" stroke="var(--blue-dark)" stroke-width="9" stroke-linecap="round"/></svg>
      <h2>SEO-Optimierung</h2>
      <p>Wir optimieren Ihre Webseite nach den <em>aktuellen Richtlinien</em> der Suchmaschinen. Struktur, Inhalte und Technik werden so angepasst, dass Sie dauerhaft bessere Platzierungen erreichen.</p>
    </article>
    <article class="service">
      <svg width="70" height="70" viewBox="0 0 70 70"><path d="M35 8C19 8 7 18 7 31c0 7 4 13 10 17l-3 12 13-8c3 1 5 1 8 1 16 0 28-10 28-23S51 8 35 8z" fill="none" stroke="var(--blue-dark)" stroke-width="5"/><line x1="23" y1="26" x2="47" y2="26" stroke="var(--blue-dark)" stroke-width="5"/><line x1="23" y1="36" x2="47" y2="36" stroke="var(--blue-dark)" stroke-width="5"/></svg>
      <h2>Consulting</h2>
      <p>Damit Sie den <em>Überblick über die</em> Arbeiten und <em>den Verlauf</em> der Webseite behalten, die wir beschlossen haben, erhalten Sie in regelmäßigen Abständen Reportings.</p>
    </article>
  </section>
</div>
</body>
</html>
```